Business card for STEADYWAVE

Please design professional business card for IT consulting firm STEADYWAVE INC.
Use logo attached.
Use information from sample qNode business card attached.
replace qnode inc with STEADYWAVE INC.
as well as qnodeinc.com with steadywave.example

```html
<!DOCTYPE html>
<html lang="en">
<head>
<meta charset="utf-8">
<title>STEADYWAVE business card</title>
<link rel="stylesheet" href="https://fonts.googleapis.com/css2?family=Jost:wght@400;500;600;700&display=swap">
<style>
  :root {
    --backdrop: #b1b1b1;
    --ink: #000000;
    --paper: #ffffff;
    --cyan: #45d6ec;
    --violet: #8a2be2;
    --magenta: #b42bb8;
    --orange: #f28a2e;
    --spectrum: linear-gradient(90deg, var(--cyan) 0%, #5f8ff0 25%, var(--violet) 45%, var(--magenta) 62%, #d8605c 80%, var(--orange) 100%);
  }
  * { box-sizing: border-box; margin: 0; padding: 0; }
  html, body { width: 1075px; height: 1200px; overflow: hidden; }
  body {
    position: relative;
    background: var(--backdrop);
    font-family: "Jost", sans-serif;
  }
  .card {
    position: absolute;
    left: 206px;
    width: 663px;
    background: var(--ink);
    color: var(--paper);
    overflow: hidden;
  }
  .card--front { top: 187px; height: 394px; }
  .card--back { top: 637px; height: 396px; }

  .brand-panel {
    position: absolute;
    left: 0; top: 0;
    width: 289px; height: 100%;
    background: var(--paper);
  }
  .brand-panel__name {
    position: absolute;
    left: 136px; top: 198px;
    transform: translate(-50%, -50%) rotate(-90deg);
    font-weight: 600;
    font-size: 35px;
    letter-spacing: 4px;
    color: var(--ink);
    white-space: nowrap;
  }
  .accent-tab {
    position: absolute;
    left: 272px; top: 0;
    width: 33px; height: 95px;
    border-radius: 0 0 17px 17px;
    background: linear-gradient(180deg, var(--orange) 0%, var(--magenta) 35%, var(--violet) 60%, var(--cyan) 100%);
  }
  .identity {
    position: absolute;
    left: 320px; top: 37px;
    line-height: 1.15;
  }
  .identity__name { font-weight: 700; font-size: 19px; }
  .identity__name span { font-weight: 400; }
  .identity__role { font-size: 19px; font-weight: 400; }

  .contact-list { list-style: none; }
  .contact {
    position: absolute;
    left: 270px;
    display: flex;
    align-items: center;
    gap: 4px;
    font-size: 19px;
  }
  .contact__icon {
    width: 38px; height: 38px;
    flex: none;
  }
  .contact--phone { top: 128px; }
  .contact--mobile { top: 161px; }
  .contact--email { top: 196px; }
  .contact--web { top: 230px; }
  .contact--address { top: 280px; align-items: flex-start; }
  .contact--address .contact__icon { margin-top: 0; }
  .address { font-style: normal; line-height: 1.25; }
  .address strong { font-weight: 700; display: block; }

  .back-name {
    position: absolute;
    left: 50%; top: 199px;
    transform: translate(-50%, -50%);
    font-weight: 600;
    font-size: 52px;
    letter-spacing: 6px;
    white-space: nowrap;
  }
  .spectrum-band {
    position: absolute;
    left: 0; bottom: 0;
    width: 100%; height: 21px;
    background: var(--spectrum);
  }
</style>
</head>
<body>
  <svg width="0" height="0" style="position:absolute">
    <defs>
      <linearGradient id="icon-grad" x1="0" y1="0" x2="1" y2="1">
        <stop offset="0" stop-color="#f28a2e"/>
        <stop offset="0.5" stop-color="#8a2be2"/>
        <stop offset="1" stop-color="#45d6ec"/>
      </linearGradient>
    </defs>
  </svg>

  <section class="card card--front">
    <div class="brand-panel">
      <div class="brand-panel__name">STEADYWAVE</div>
    </div>
    <div class="accent-tab"></div>

    <div class="identity">
      <p class="identity__name">MIKHAIL DOROVSKY, <span>P.ENG.</span></p>
      <p class="identity__role">General Manager</p>
    </div>

    <ul class="contact-list">
      <li class="contact contact--phone">
        <svg class="contact__icon" viewBox="0 0 38 38"><circle cx="19" cy="19" r="17.5" fill="#000" stroke="#fff" stroke-width="1.5"/><path d="M13 12 l3-1 2 4-2 1.5 a9 9 0 0 0 4.5 4.5 l1.5-2 4 2-1 3 c-7 0-12-5-12-12z" fill="url(#icon-grad)"/></svg>
        <span>(905)555-0142 ext.201</span>
      </li>
      <li class="contact contact--mobile">
        <svg class="contact__icon" viewBox="0 0 38 38"><circle cx="19" cy="19" r="17.5" fill="#000" stroke="#fff" stroke-width="1.5"/><rect x="14" y="11" width="10" height="16" rx="1.5" fill="none" stroke="url(#icon-grad)" stroke-width="2"/><circle cx="19" cy="24" r="1" fill="#45d6ec"/></svg>
        <span>(416)555-0187</span>
      </li>
      <li class="contact contact--email">
        <svg class="contact__icon" viewBox="0 0 38 38"><circle cx="19" cy="19" r="17.5" fill="#000" stroke="#fff" stroke-width="1.5"/><rect x="11" y="13" width="16" height="12" fill="url(#icon-grad)"/><path d="M11 13 l8 6 8-6" fill="none" stroke="#fff" stroke-width="1.2"/></svg>
        <span>mdorovsky@steadywave.example</span>
      </li>
      <li class="contact contact--web">
        <svg class="contact__icon" viewBox="0 0 38 38"><circle cx="19" cy="19" r="17.5" fill="#000" stroke="#fff" stroke-width="1.5"/><g fill="none" stroke="url(#icon-grad)" stroke-width="1.6"><circle cx="19" cy="19" r="8"/><ellipse cx="19" cy="19" rx="3.5" ry="8"/><path d="M11 19h16M12.5 15h13M12.5 23h13"/></g></svg>
        <span>www.steadywave.example</span>
      </li>
      <li class="contact contact--address">
        <svg class="contact__icon" viewBox="0 0 38 38"><circle cx="19" cy="19" r="17.5" fill="#000" stroke="#fff" stroke-width="1.5"/><path d="M19 29 c-5-6-7-9-7-12 a7 7 0 0 1 14 0 c0 3-2 6-7 12z" fill="url(#icon-grad)"/><circle cx="19" cy="17" r="2.5" fill="#fff"/></svg>
        <address class="address">
          <strong>STEADYWAVE INC.</strong>
          1820 Harbourline Rd., Suite 101<br>
          Oakridge, Ontario, L4K2P9, Canada
        </address>
      </li>
    </ul>
  </section>

  <section class="card card--back">
    <div class="back-name">STEADYWAVE</div>
    <div class="spectrum-band"></div>
  </section>
</body>
</html>
```